Business Card Design

Company is a Commercial Building Company specialising in New Construction and existing refurbishments

Business

Contact Information for Business Card

Derek Halloway
Construction Manager
E Derek@ridgemarkbuilding.com.au
M 0400 215 397
Mail 14 Tarrington Loop Harbourton WA 6190

```html
<!DOCTYPE html>
<html lang="en">
<head>
<meta charset="utf-8">
<title>Ridgemark Building &amp; Construction – Business Card</title>
<link rel="stylesheet" href="https://fonts.googleapis.com/css2?family=Roboto:wght@300;400&family=Roboto+Condensed:wght@700&display=swap">
<style>
  :root{
    --bg:#e9e7e3;
    --paper:#ffffff;
    --navy:#2f3749;
    --cyan:#08b8d6;
    --ink:#2f3749;
    --white:#ffffff;
    --photo-grey-a:#f3f3f1;
    --photo-grey-b:#a9a59d;
    --sky-a:#cfe6f3;
    --sky-b:#b9b3e0;
    --sky-c:#9d86c9;
  }
  *{box-sizing:border-box;margin:0;padding:0}
  html,body{width:1200px;height:858px;overflow:hidden;background:var(--bg)}
  body{display:flex;flex-direction:column;align-items:center;justify-content:center;gap:36px;font-family:"Roboto",Arial,sans-serif}
  .card{position:relative;width:620px;height:379px;background:var(--paper);overflow:hidden;box-shadow:0 4px 14px rgba(0,0,0,.18)}

  /* front */
  .card-front .building-photo{position:absolute;left:34%;top:0;width:38%;height:64%;
    background:linear-gradient(160deg,var(--photo-grey-a) 10%,#d9d7d2 45%,var(--photo-grey-b) 100%)}
  .card-front .gap-band{position:absolute;inset:0;background:var(--paper);
    clip-path:polygon(34% 57%,100% 45%,100% 100%,34% 100%)}
  .card-front .name-band{position:absolute;inset:0;background:var(--cyan);
    clip-path:polygon(66% 0,100% 0,100% 46%,52% 57%)}
  .card-front .contact-band{position:absolute;inset:0;background:var(--navy);
    clip-path:polygon(37% 61%,100% 50%,100% 100%,37% 100%)}
  .holder{position:absolute;right:24px;top:92px;text-align:right;color:var(--navy)}
  .holder-name{font-size:30px;font-weight:400;line-height:1.1;letter-spacing:-.3px}
  .holder-title{font-size:14px;font-weight:300;color:var(--white);margin-top:4px}
  .contacts{position:absolute;left:41%;top:68%;list-style:none;color:var(--white);font-size:14px;font-weight:300}
  .contacts li{display:flex;align-items:center;gap:12px;height:28px;white-space:nowrap}
  .contacts svg{width:14px;height:14px;fill:var(--cyan);flex:none}
  .brand{position:absolute;left:34px;top:200px;display:flex;align-items:center;gap:10px}
  .brand-mark{width:22px;height:22px;background:var(--cyan);flex:none}
  .brand-name{font-family:"Roboto Condensed",Arial,sans-serif;font-weight:700;font-size:16px;line-height:1.2;color:var(--ink);text-transform:uppercase;letter-spacing:.3px}

  /* back */
  .card-back .skyline-photo{position:absolute;inset:0;
    background:linear-gradient(170deg,var(--sky-a) 0%,#c8dcef 40%,var(--sky-b) 75%,var(--sky-c) 100%)}
  .card-back .brand{left:auto;right:36px;top:36px}
</style>
</head>
<body>

<section class="card card-front" aria-label="Business card front">
  <div class="building-photo" role="img" aria-label="Photo of a white multi-storey apartment building with curved balconies"></div>
  <div class="gap-band"></div>
  <div class="name-band"></div>
  <div class="contact-band"></div>

  <div class="brand">
    <span class="brand-mark"></span>
    <span class="brand-name">Ridgemark Building<br>&amp; Construction</span>
  </div>

  <div class="holder">
    <p class="holder-name">Derek Halloway</p>
    <p class="holder-title">Construction Manager</p>
  </div>

  <ul class="contacts">
    <li><svg viewBox="0 0 24 24" aria-hidden="true"><path d="M6.6 10.8a15 15 0 0 0 6.6 6.6l2.2-2.2c.3-.3.7-.4 1-.2 1.1.4 2.3.6 3.6.6.6 0 1 .4 1 1V20c0 .6-.4 1-1 1A17 17 0 0 1 3 4c0-.6.4-1 1-1h3.5c.6 0 1 .4 1 1 0 1.3.2 2.5.6 3.6.1.3 0 .7-.2 1z"/></svg>0400 215 397</li>
    <li><svg viewBox="0 0 24 24" aria-hidden="true"><path d="M2 5h20v14H2zm2 2v.5l8 5 8-5V7zm0 2.8V17h16V9.8l-8 5z"/></svg>Derek@ridgemarkbuilding.com.au</li>
    <li><svg viewBox="0 0 24 24" aria-hidden="true"><path d="M12 2a7 7 0 0 0-7 7c0 5 7 13 7 13s7-8 7-13a7 7 0 0 0-7-7zm0 9.5A2.5 2.5 0 1 1 12 6.5a2.5 2.5 0 0 1 0 5z"/></svg>14 Tarrington Loop Harbourton WA 6190</li>
  </ul>
</section>

<section class="card card-back" aria-label="Business card back">
  <div class="skyline-photo" role="img" aria-label="Photo of a city skyline at dusk with a curved glass tower lit in gold"></div>
  <div class="brand">
    <span class="brand-mark"></span>
    <span class="brand-name">Ridgemark Building<br>&amp; Construction</span>
  </div>
</section>

</body>
</html>
```